Business Card Design Project

I am looking for a classy business card design for a product design consultancy. We specialize in Product Design, Prototyping, and Manufacturing Consulting. Products that we design range from consumer electronics to household products all the way to sporting goods. We are based in Arizona and called "Pelican Forge Studio." We like to have fun and goof off as much as we like to create new products. We are young and energetic so we would like our business cards to reflect that. We already have a logo that we would like to implement into the card design. A plain rectangular business card is boring so feel free to get creative, but please, no avocado shaped cards (it's far too literal). Also feel free to play around with textured card stocks or plastic. The final design that we choose will pay attention to all of the little details. Our cards will need to be 2 sided. We're giving you guys free reign to design as you would like. Please have fun with this, it will reflect in our business card.

Thanks guys,
Pelican Forge Studio Team
Updates

Industry/Entity Type

Electronics

Requirements
Must have
• We would like to have a spot UV coating somewhere on the business card design if possible.
Nice to have
• Let's see some designs with custom shapes rather than typical rectangular business cards but please no avocado shaped cards, thanks. Also play around with textured card socks.

Files

```html
<!DOCTYPE html>
<html lang="en">
<head>
<meta charset="utf-8">
<title>Pelican Forge Studio – Business Card</title>
<link rel="stylesheet" href="https://fonts.googleapis.com/css2?family=Questrial&display=swap">
<style>
  :root {
    --backdrop: #2e2e30;
    --lime: #8dc63f;
    --lime-light: #9fd14f;
    --lime-deep: #79b12c;
    --paper: #f4f4f2;
    --ink: #2a2a2a;
    --white: #ffffff;
  }
  * { margin: 0; padding: 0; box-sizing: border-box; }
  html, body {
    width: 1200px; height: 716px; overflow: hidden;
    background: var(--backdrop);
    font-family: "Questrial", "Helvetica Neue", Arial, sans-serif;
  }
  .sheet {
    position: relative; width: 1200px; height: 716px;
    display: flex; align-items: center; justify-content: center; gap: 50px;
  }
  .card {
    position: relative; width: 540px; height: 309px;
    border-radius: 4px; overflow: hidden;
    box-shadow: 0 14px 30px rgba(0,0,0,.45);
  }
  /* Front side */
  .card--front {
    background: linear-gradient(135deg, var(--lime-light) 0%, var(--lime) 55%, var(--lime-deep) 100%);
    color: var(--white);
  }
  .card--front .brand-name {
    position: absolute; left: 250px; top: 112px;
    font-size: 27px; letter-spacing: 1px; color: var(--white); white-space: nowrap;
  }
  .services {
    position: absolute; left: 252px; top: 166px; list-style: none;
    font-size: 12px; letter-spacing: .6px; text-transform: uppercase; line-height: 19px;
  }
  .services li { display: flex; align-items: center; gap: 7px; }
  .services svg { width: 7px; height: 7px; flex: none; }
  /* Back side */
  .card--back { background: var(--paper); color: var(--ink); }
  .brand-lockup {
    position: absolute; left: 34px; top: 34px;
    display: flex; align-items: center; gap: 12px;
  }
  .brand-lockup svg { width: 34px; height: 34px; }
  .card--back .brand-name { font-size: 32px; color: var(--lime); letter-spacing: .5px; white-space: nowrap; }
  .person { position: absolute; left: 34px; top: 140px; }
  .person-name { font-size: 19px; color: var(--lime); text-transform: uppercase; letter-spacing: .6px; }
  .person-role { font-size: 12px; text-transform: uppercase; letter-spacing: .5px; margin-top: 1px; }
  .phones { position: absolute; left: 34px; top: 196px; font-size: 12.5px; line-height: 16px; }
  .address { position: absolute; left: 320px; top: 196px; font-size: 12.5px; line-height: 16px; }
  .online { position: absolute; left: 320px; top: 248px; font-size: 12.5px; line-height: 16px; }
</style>
</head>
<body>
<main class="sheet">
  <section class="card card--front" aria-label="Card front">
    <div class="brand-name">Pelican Forge Studio</div>
    <ul class="services">
      <li><svg viewBox="0 0 8 8"><circle cx="4" cy="4" r="4" fill="#ffffff"/></svg>Product Design</li>
      <li><svg viewBox="0 0 8 8"><circle cx="4" cy="4" r="4" fill="#ffffff"/></svg>Prototyping</li>
      <li><svg viewBox="0 0 8 8"><circle cx="4" cy="4" r="4" fill="#ffffff"/></svg>Manufacturing Consulting</li>
    </ul>
  </section>

  <section class="card card--back" aria-label="Card back">
    <div class="brand-lockup">
      <svg viewBox="0 0 34 34" aria-hidden="true"><circle cx="17" cy="17" r="17" fill="#8dc63f"/></svg>
      <span class="brand-name">Pelican Forge Studio</span>
    </div>
    <div class="person">
      <div class="person-name">Marcus Delrey</div>
      <div class="person-role">Managing Director</div>
    </div>
    <div class="phones">480 555 01 27<br>480 555 01 94</div>
    <div class="address">48 Kiln Road<br>Tempe, Arizona 85281</div>
    <div class="online">hello@pelicanforge.studio<br>www.pelicanforge.studio</div>
  </section>
</main>
</body>
</html>
```